Tavo Payments Business card refresh

Need a new design of our business card The info is not what is on these cards i sent this for a reference. I can email all the info over
Info would be Derek Whitfield Chief TAVO is the title. our new address is 47615 Birch Hollow Rd. Westlake Village Ca 91384 Cell number is 805-634-2917 Work number is 855-482-7309 ext 212 Derek@tavopayments.com is my email address
Target Market(s)
Merchant Services all businesses that take credit cards
Industry/Entity Type
Merchant Services / Credit Card processing
Contact Information for Business Card
Need a new design of our business card The info is not what is on these cards i sent this for a reference. I can email all the info over Info would be Derek Whitfield Chief TAVO is the title. our new address is 47615 Birch Hollow Rd. Westlake Village Ca 91384 Cell number is 805-634-2917 Work number is 855-482-7309 ext 212 Derek@tavopayments.com is my email address
Requirements
Must have
- My logo and colors from my brand guidelines
Nice to have
- i sent some designs just need a new refresh
Should not have
- nothing specific

```html
<!DOCTYPE html>
<html lang="en">
<head>
<meta charset="utf-8">
<title>Tavo Payments – Business Card</title>
<link href="https://fonts.googleapis.com/css2?family=Montserrat:wght@400;500;600;800&display=swap" rel="stylesheet">
<style>
  :root {
    --ink: #272d31;
    --lime: #97c300;
    --white: #ffffff;
    --backdrop: #e2e2e2;
  }
  * { box-sizing: border-box; margin: 0; padding: 0; }
  html, body {
    width: 1200px; height: 1200px; overflow: hidden;
    background: var(--backdrop);
    font-family: "Montserrat", sans-serif;
  }
  .card {
    position: absolute; left: 276px;
    width: 649px; height: 372px;
    overflow: hidden;
  }
  .card--front { top: 185px; background: var(--ink); }
  .card--back { top: 642px; background: var(--ink); }
  .card__shape { position: absolute; inset: 0; width: 100%; height: 100%; }

  .brand-name {
    position: absolute; left: 45px; top: 162px; width: 220px;
    text-align: center;
    color: var(--white); font-weight: 600; font-size: 30px; letter-spacing: 0.5px;
  }

  .promises {
    position: absolute; left: 419px; top: 104px;
    list-style: none;
    color: var(--white); font-weight: 800; font-size: 21px; line-height: 30px;
  }
  .promises li::before {
    content: ""; display: inline-block; width: 8px; height: 8px; border-radius: 50%;
    background: var(--white); margin-right: 10px; vertical-align: middle; position: relative; top: -2px;
  }
  .referral {
    position: absolute; left: 419px; top: 197px;
    color: var(--white); font-weight: 500; font-size: 15.5px; line-height: 23px;
  }

  .person-name {
    position: absolute; left: 269px; top: 56px;
    color: var(--lime); font-weight: 800; font-size: 32px; letter-spacing: -0.3px;
  }
  .person-title {
    position: absolute; left: 269px; top: 110px;
    color: var(--white); font-weight: 500; font-size: 19px;
  }
  .contacts { position: absolute; left: 269px; top: 172px; list-style: none; }
  .contacts li {
    display: flex; align-items: flex-start;
    color: var(--white); font-weight: 500; font-size: 18px; line-height: 28px;
    margin-bottom: 8px;
  }
  .contacts li:nth-child(1) { margin-bottom: 9px; }
  .contacts .icon { width: 24px; height: 24px; margin: 2px 12px 0 0; flex: none; fill: var(--lime); }
</style>
</head>
<body>

<section class="card card--front" aria-label="Card front">
  <svg class="card__shape" viewBox="0 0 1045 599" preserveAspectRatio="none" aria-hidden="true">
    <polygon fill="var(--white)" points="667,0 1045,0 1045,599 379,599 486,289 503,287 566,322" />
    <polygon fill="var(--lime)" points="687,0 1045,0 1045,599 401,599 503,287 586,322" />
  </svg>
  <div class="brand-name">TAVO Payments</div>
  <ul class="promises">
    <li>BEST RATES</li>
    <li>BEST SERVICE</li>
    <li>GUARANTEED</li>
  </ul>
  <p class="referral">Ask about our<br>“Merchant Referral”<br>Program</p>
</section>

<section class="card card--back" aria-label="Card back">
  <svg class="card__shape" viewBox="0 0 1045 599" preserveAspectRatio="none" aria-hidden="true">
    <polygon fill="var(--white)" points="0,0 410,0 309,312 289,312 221,276 241,276 122,599 0,599" />
    <polygon fill="var(--lime)" points="0,0 390,0 289,312 221,276 102,599 0,599" />
  </svg>
  <h1 class="person-name">Derek Whitfield</h1>
  <p class="person-title">Chief Sales Office</p>
  <ul class="contacts">
    <li>
      <svg class="icon" viewBox="0 0 24 24" aria-hidden="true"><path d="M12 2 1 12h3v10h6v-6h4v6h6V12h3z"/></svg>
      <span>47615 Birch Hollow Rd.<br>Westlake Village Ca 91384</span>
    </li>
    <li>
      <svg class="icon" viewBox="0 0 24 24" aria-hidden="true"><path d="M7 1h10a2 2 0 0 1 2 2v18a2 2 0 0 1-2 2H7a2 2 0 0 1-2-2V3a2 2 0 0 1 2-2zm0 3v14h10V4zm5 15.5a1.2 1.2 0 1 0 0 2.4 1.2 1.2 0 0 0 0-2.4z"/></svg>
      <span>805-634-2917</span>
    </li>
    <li>
      <svg class="icon" viewBox="0 0 24 24" aria-hidden="true"><path d="M2 8c0-3 5-5 10-5s10 2 10 5v2h-5V8c-1-.7-3-1-5-1s-4 .3-5 1v2H2zm6 3h8l4 4v6H4v-6zm4 2a3 3 0 1 0 0 6 3 3 0 0 0 0-6z"/></svg>
      <span>855-482-7309 ext 212</span>
    </li>
    <li>
      <svg class="icon" viewBox="0 0 24 24" aria-hidden="true"><path d="M2 5h20v14H2zm2 2v.5l8 6 8-6V7l-8 6z"/></svg>
      <span>Derek@tavopayments.com</span>
    </li>
  </ul>
</section>

</body>
</html>
```